Velorin business card design

Design a business card for a cryptocurrency company that uses the attached logo. Some example business cards to give you guys a flavor of what we're looking for is given below (of course feel free to be creative):
https://www.plumcardhub.example/studio.aspx?template=4819265_KT3&ag=True&xnav=HSG_Design_Image&rd=1
https://www.plumcardhub.example/studio.aspx?template=3027514_KT3&ag=True&xnav=HSG_Design_Image&rd=1
The business card should be clean/simple and convey the company name, what we're about and the specific persons contact info. In terms of what we're about, we can have our name Velorin, with a line under it that says "Cryptocurrency visualization, analytics, and trading"
We want something futuristic looking but simple / clean.
The color scheme for the logo should be used.
The name of the person and their title should be editable, so we can use the business card design for multiple people.
(Please use the zip file to get the vector graphics and different image formats)

```html
<!DOCTYPE html>
<html lang="en">
<head>
<meta charset="utf-8">
<title>Velorin business card</title>
<link href="https://fonts.googleapis.com/css2?family=Jost:wght@300;400;500;600&display=swap" rel="stylesheet">
<style>
  :root {
    --page: #eeeeec;
    --card: #dcdcd8;
    --navy: #1a2238;
    --green: #2fae6a;
    --teal: #1e9a9a;
    --ink: #1c1c22;
  }
  html, body {
    margin: 0;
    width: 1176px;
    height: 1200px;
    overflow: hidden;
    background: var(--page);
    font-family: "Jost", sans-serif;
  }
  .card {
    position: absolute;
    left: 88px;
    top: 314px;
    width: 1000px;
    height: 571px;
    background: var(--card);
    box-shadow: 0 6px 18px rgba(0,0,0,0.12);
  }
  .brand {
    position: absolute;
    left: 110px;
    top: 250px;
    display: flex;
    align-items: center;
    gap: 18px;
  }
  .brand-dot {
    width: 44px;
    height: 44px;
    border-radius: 50%;
    background: var(--green);
  }
  .brand-name {
    font-weight: 600;
    font-size: 66px;
    letter-spacing: 6px;
    color: var(--navy);
    text-transform: uppercase;
    line-height: 1;
  }
  .tagline {
    position: absolute;
    left: 130px;
    top: 345px;
    width: 400px;
    text-align: center;
    font-size: 17px;
    letter-spacing: 1.5px;
    color: var(--ink);
    text-transform: uppercase;
    line-height: 1.45;
  }
  .divider {
    position: absolute;
    left: 560px;
    top: 80px;
    width: 2px;
    height: 390px;
    background: var(--teal);
  }
  .person {
    position: absolute;
    left: 600px;
    top: 100px;
  }
  .person-name {
    font-size: 42px;
    color: var(--navy);
    line-height: 1;
    text-transform: uppercase;
  }
  .person-name .first { font-weight: 600; }
  .person-name .last { font-weight: 300; }
  .person-title {
    font-size: 22px;
    color: var(--green);
    text-transform: uppercase;
    margin-top: 2px;
    letter-spacing: 0.5px;
  }
  .contacts {
    list-style: none;
    margin: 18px 0 0 22px;
    padding: 0;
  }
  .contacts li {
    display: flex;
    align-items: center;
    gap: 16px;
    font-size: 22px;
    font-weight: 500;
    color: var(--ink);
    height: 36px;
  }
  .contacts svg { width: 22px; height: 22px; flex: none; }
  .address {
    position: absolute;
    left: 600px;
    top: 445px;
    font-size: 22px;
    font-weight: 600;
    color: var(--ink);
  }
</style>
</head>
<body>
  <div class="card">
    <div class="brand">
      <span class="brand-dot"></span>
      <span class="brand-name">Velorin</span>
    </div>
    <p class="tagline">Cryptocurrency visualization,<br>analytics, and trading</p>

    <div class="divider"></div>

    <div class="person">
      <div class="person-name"><span class="first">Marek</span> <span class="last">Doyle</span></div>
      <div class="person-title">President</div>
      <ul class="contacts">
        <li>
          <svg viewBox="0 0 24 24" aria-hidden="true"><path fill="#2fae6a" d="M6.6 10.8a15.1 15.1 0 0 0 6.6 6.6l2.2-2.2a1 1 0 0 1 1-.25 11.4 11.4 0 0 0 3.6.57 1 1 0 0 1 1 1V20a1 1 0 0 1-1 1A17 17 0 0 1 3 4a1 1 0 0 1 1-1h3.5a1 1 0 0 1 1 1c0 1.25.2 2.46.57 3.6a1 1 0 0 1-.25 1z"/></svg>
          +91 98 76 543210
        </li>
        <li>
          <svg viewBox="0 0 24 24" aria-hidden="true" fill="none" stroke="#2fae6a" stroke-width="1.8"><circle cx="12" cy="12" r="9"/><ellipse cx="12" cy="12" rx="4" ry="9"/><path d="M3 12h18M5 7h14M5 17h14"/></svg>
          www.velorin.example
        </li>
        <li>
          <svg viewBox="0 0 24 24" aria-hidden="true"><rect x="2" y="5" width="20" height="14" fill="#2fae6a"/><path d="M2 5l10 8 10-8" fill="none" stroke="#dcdcd8" stroke-width="1.6"/></svg>
          info@velorin.example
        </li>
      </ul>
    </div>

    <div class="address">P.o.box 48 - Reno,USA</div>
  </div>
</body>
</html>
```